Mexican Restaurant needs a new Menu Design

Mexican restaurant LA TORTUGA VERDE is renewing its menu, so we need something new.
Since our inception we have given the task of rescuing ingredients, recipes, and traditional and representatives dishes of the culinary techniques of yesteryear.
We are the only restaurant in Guadalajara that manufactures its own dairy natural as fresh cheese, the cream and our already well-known and traditional jocoqui. In addition, we produce organic ranch egg and are currently in the development of organic vegetables cultivated on the slopes of the old Hill which gives our plants benefit from an exceptional microclimate.
Find more information about the restaurant in www.latortugaverde.com.
The menu needs to have the full list of products with the prices, some phrases that speak of the philosophy of the ranch-style-living, photos.
We need the cover, back cover and interiors.
Updates
Thank you so much for the proposals you have submitted for the menu design. We are looking them carefully.
Thank you very much for taking your time to design a proposal for our menu!!!
Target Market(s)
The target is very wide (28-40 yrs.): Young executives, Young families, Housewives.
Industry/Entity Type
Restaurant
Look and feel
Each slider illustrates characteristics of the customer's brand and the style your logo design should communicate.

```html
<!DOCTYPE html>
<html lang="es">
<head>
<meta charset="utf-8">
<title>La Tortuga Verde — Menú páginas 5 y 6</title>
<link href="https://fonts.googleapis.com/css2?family=Cabin:wght@400;500&family=Alegreya:wght@700&display=swap" rel="stylesheet">
<style>
  :root{
    --canvas:#efefef;
    --frame:#e5211d;
    --paper-light:#f7ebc8;
    --paper-dark:#ecd8a6;
    --ink:#2c2418;
    --ink-soft:#3b3226;
    --rule:#5a4d3c;
    --label:#6a5c48;
    --badge:#e3221f;
    --strip-dark:#2a0f0a;
    --strip-mid:#5a1a10;
  }
  *{margin:0;padding:0;box-sizing:border-box}
  html,body{width:1200px;height:901px;overflow:hidden;background:var(--canvas)}
  .spread{position:relative;width:1200px;height:901px}
  .page{position:absolute;top:30px;width:569px;height:727px;border:4px solid var(--frame);
    background:radial-gradient(ellipse at 30% 20%,var(--paper-light),var(--paper-dark) 90%)}
  .page--left{left:22px}
  .page--right{left:609px}
  .page__number{position:absolute;top:6px;right:12px;font:400 16px "Alegreya",Georgia,serif;color:var(--label);font-weight:400}
  .dish{position:absolute;left:12px;right:14px}
  .dish__head{display:flex;justify-content:space-between;height:26px;line-height:22px;padding:0 4px 0 2px;
    border-bottom:1px solid var(--rule);font:400 17px "Cabin",sans-serif;color:var(--ink)}
  .dish__price{letter-spacing:.5px}
  .dish__desc{margin-top:3px;padding-left:2px;font:400 13px/17px "Cabin",sans-serif;color:var(--ink-soft)}
  .section-title{position:absolute;height:34px;line-height:34px;padding:0 10px;background:var(--badge);
    border-radius:14px 6px 16px 8px;color:#fff;font:700 25px "Alegreya",Georgia,serif;white-space:nowrap}
  .photo-strip{position:absolute;top:755px;height:102px;
    background:linear-gradient(90deg,var(--strip-dark),var(--strip-mid) 30%,var(--strip-dark) 55%,var(--strip-mid) 80%,var(--strip-dark))}
  .photo-strip--left{left:22px;width:569px}
  .photo-strip--right{left:609px;width:569px}
</style>
</head>
<body>
<div class="spread">

  <section class="page page--left">
    <span class="page__number">page 5</span>

    <div class="dish" style="top:45px">
      <div class="dish__head"><span>Gorditas Surtidas</span><span class="dish__price">00.00</span></div>
      <p class="dish__desc">Gorditas, Gorditas pero están Rebuenas! Rellenas de Frijolitos, Rajas y Chicharrón de Carnitas´n.</p>
    </div>
    <div class="dish" style="top:116px">
      <div class="dish__head"><span>Gorditas con Frijolitos´n</span><span class="dish__price">00.00</span></div>
      <p class="dish__desc">Rellenas de Frijolitos de La Casa y Bañadas en Salsita Roja sin Picante.</p>
    </div>
    <div class="dish" style="top:175px">
      <div class="dish__head"><span>Gorditas Estilo Doña Chela</span><span class="dish__price">00.00</span></div>
      <p class="dish__desc">Con mantequilla Artesanal de Los Altos y Sal. Se recomienda Sopearlas en Atole o Champurrado como en San Miguel.</p>
    </div>
    <div class="dish" style="top:252px">
      <div class="dish__head"><span>Gorditas con Rajas y Panela</span><span class="dish__price">00.00</span></div>
      <p class="dish__desc">¡Que Rajas y Que Panela!</p>
    </div>

    <h2 class="section-title" style="top:303px;left:8px">Molletes y semas</h2>

    <div class="dish" style="top:353px">
      <div class="dish__head"><span>Molletes Dulces</span><span class="dish__price">00.00</span></div>
      <p class="dish__desc">Con mantequilla artesanal de Los Altos y azúcar.</p>
    </div>
    <div class="dish" style="top:413px">
      <div class="dish__head"><span>Molletes con Chilaquiles´n</span><span class="dish__price">00.00</span></div>
      <p class="dish__desc">Con Chilaquiles de cualquiera de nuestras especialidades al Queso Gratinao (O gratín que es lo mesmo).</p>
    </div>
    <div class="dish" style="top:483px">
      <div class="dish__head"><span>Molletes Supremos de Natas</span><span class="dish__price">00.00</span></div>
      <p class="dish__desc">¡ Nuestras Natas son para presumirse ! 100% Natas de Leche 100% de Vaca.</p>
    </div>
    <div class="dish" style="top:541px">
      <div class="dish__head"><span>Molletes de Frijoles Gratinados</span><span class="dish__price">00.00</span></div>
      <p class="dish__desc">Con nuestros Frijolitos de La Casa y Gratinaos con nuestro muy mentao Queso Gratín Artesanal.</p>
    </div>

    <h2 class="section-title" style="top:604px;left:9px">De juera</h2>

    <div class="dish" style="top:653px">
      <div class="dish__head"><span>Orden de Fruta de la Estación</span><span class="dish__price">00.00</span></div>
      <p class="dish__desc">Papaya, Piña, Melón y Manzana. La más Saludable manera Pa´iniciar su Desayuno.</p>
    </div>
  </section>

  <section class="page page--right">
    <span class="page__number">page 6</span>

    <div class="dish" style="top:44px">
      <div class="dish__head"><span>Hot Cakes</span><span class="dish__price">00.00</span></div>
      <p class="dish__desc">En San Miguel les decimos "Quequis". Van con miel de abeja, miel de maple, mermelada de fresa, tocino o jamón.</p>
    </div>
    <div class="dish" style="top:120px">
      <div class="dish__head"><span>Orden de Yogur Artesanal con Fruta, Granola y Miel</span><span class="dish__price">00.00</span></div>
      <p class="dish__desc">Muy Saludable Yogur Artesanal elaborado por nosotros sin Conservadores. Va con Frutita de la Estación ¡Puros Lactobacilos 100% Naturales´n !</p>
    </div>

    <h2 class="section-title" style="top:192px;left:12px">Desayuno infantil</h2>

    <div class="dish" style="top:249px">
      <div class="dish__head"><span>Hot Cakes Infantiles</span><span class="dish__price">00.00</span></div>
      <p class="dish__desc">En San Miguel Les decimos "Quequis". Van con Miel de Abeja o Miel de Maple (O con las Dos) y Mantequilla.</p>
    </div>

    <h2 class="section-title" style="top:317px;left:15px">Pa´ Empezar</h2>

    <div class="dish" style="top:373px;left:14px">
      <div class="dish__head"><span>Guacamole estilo "Teocuitatlán"</span><span class="dish__price">00.00</span></div>
      <p class="dish__desc">Con Queso Cotija y un toque de Chile de Árbol.</p>
    </div>
    <div class="dish" style="top:433px;left:14px">
      <div class="dish__head"><span>Guacamole Tradicional</span><span class="dish__price">00.00</span></div>
      <p class="dish__desc">Con Chilito Verde, Cebolla, Cilantro, Jitomate y Panelita Artesanal.</p>
    </div>
    <div class="dish" style="top:493px;left:14px">
      <div class="dish__head"><span>Queso Fundido con Pastor</span><span class="dish__price">00.00</span></div>
      <p class="dish__desc">Queso Gratin de los Altos de Jalisco Con Jugoso Cerdito al Pastor.</p>
    </div>
    <div class="dish" style="top:556px;left:14px">
      <div class="dish__head"><span>Queso Fundido con Champiñones</span><span class="dish__price">00.00</span></div>
      <p class="dish__desc">Queso Gratín Elaborado en Los Meritítos Altos de Jalisco con Champiñoncitos a la Plancha acompañado de Tortillitas Recién Hechas.</p>
    </div>
    <div class="dish" style="top:630px;left:14px">
      <div class="dish__head"><span>Queso Fundido con Chorizo</span><span class="dish__price">00.00</span></div>
      <p class="dish__desc">Con Chorizo Ranchero y Queso Gratín Elaborado en Los Meritítos Altos de Jalisco acompañado de Tortillitas Recién Hechas.</p>
    </div>
  </section>

  <div class="photo-strip photo-strip--left" role="img" aria-label="Fotos de platillos sobre chiles secos: gorditas, yogur con fruta, plato de fruta picada y hot cakes"></div>
  <div class="photo-strip photo-strip--right" role="img" aria-label="Fotos de platillos sobre chiles secos: guacamole, hot cakes infantiles decorados, guacamole tradicional y queso fundido con chorizo"></div>

</div>
</body>
</html>
```